The Fern Lantern Pub- restaurant menu, new launch

This is a new restaurant launching Summer 2017. Restaurant is a conversion of long standing small town existing family pizza/italian restaurant. new concept shifts concept to a family pub atmosphere featuring familiar appetizers, burgers, wood-fired pizza, and daily specials, draft beer, full- bar.

atmosphere is casual. want menu to reflect a more current "vibe" than the old place did. Not cold and modern, but retain the cozy familiar feel, without seeming dated and old fashioned.

4 panel menu; 8.5 X 11; 2-4 color
Updates

Project Deadline Extended
Reason: I am interested in seeing more designs. I will be providing feedback in the next few days on all designs submitted. I will also be increasing the budget.

Target Market(s)

Family-Oriented Pub, rural location Berkshire County, MA. Mostly Blue collar customer, value oriented

Industry/Entity Type

American Restaurant

Font styles to use
Sans Serif

Colors

Designer to choose colors to be used in the design.

Requirements
Must have
• Clear, uncluttered design, Highlighted items as specified in draft file (to come)
• ability to make changes daily as menu changes
• each panel separate sheet to slide into binder sleeve

```html
<!DOCTYPE html>
<html lang="en">
<head>
<meta charset="utf-8">
<title>The Fern Lantern Pub – Wood Fired Pizza</title>
<link rel="stylesheet" href="https://fonts.googleapis.com/css2?family=IM+Fell+English&family=Handlee&family=Didact+Gothic&display=swap">
<style>
  :root{
    --paper:#f7efe7;
    --red:#e8231f;
    --ink:#4a4240;
    --band:#554c4b;
    --sketch:#e6dcd2;
    --white:#fbf6f1;
  }
  *{margin:0;padding:0;box-sizing:border-box}
  html,body{width:927px;height:1200px;overflow:hidden;background:var(--paper)}
  .menu{position:relative;width:927px;height:1200px;background:var(--paper);color:var(--ink);font-family:"Didact Gothic",sans-serif}
  .sketch{position:absolute;background:var(--sketch);opacity:.8}
  .sketch--left{left:0;top:880px;width:125px;height:320px;border-radius:0 90px 40px 0}
  .sketch--slice{left:782px;top:740px;width:145px;height:140px;border-radius:60px 0 0 80px}
  .sketch--crust{left:866px;top:944px;width:61px;height:256px;border-radius:50px 0 0 0}

  .page-title{position:absolute;top:46px;left:0;width:100%;text-align:center;padding-left:50px;font-family:"IM Fell English",serif;font-weight:400;font-size:52px;letter-spacing:-1px;color:var(--ink)}
  .intro{position:absolute;top:108px;left:100px;width:780px;text-align:center;font-family:"Handlee",cursive;color:var(--red);font-size:16.5px;line-height:22px}

  .specialty-band{position:absolute;left:0;top:178px;width:678px;height:50px;background:var(--red);color:var(--white);font-family:"IM Fell English",serif;font-size:31px;line-height:50px;padding-left:64px;white-space:nowrap}
  .specialty-band .price{margin-left:26px;font-size:28px}

  .pie{position:absolute;text-align:center}
  .pie h2{font-family:"IM Fell English",serif;font-weight:400;font-size:42px;color:var(--ink);line-height:50px;border-bottom:2px solid var(--ink);padding-bottom:4px}
  .pie p{font-family:"Handlee",cursive;color:var(--red);font-size:18px;line-height:27px;margin-top:10px}
  .pie--buffalo{left:92px;top:262px;width:330px}
  .pie--hula{left:537px;top:262px;width:309px}
  .pie--hula p{margin-top:14px}
  .pie--chicken{left:338px;top:458px;width:260px}
  .pie--chicken p{width:340px;margin-left:-40px}

  .build{position:absolute;left:145px;top:631px;width:615px;height:515px;border:2px solid var(--band);background:var(--paper)}
  .build__head{background:var(--band);color:var(--white);text-align:center;height:96px;padding-top:8px;font-family:"IM Fell English",serif}
  .build__head h2{font-weight:400;font-size:41px;line-height:46px}
  .build__head .price{font-size:24px;line-height:28px}
  .build__body{text-align:center;font-size:17px;line-height:26px;padding-top:8px}
  .group{margin-bottom:12px}
  .cost{font-weight:700;font-size:19px}
  .label{font-weight:700}
  .note{margin-top:18px}
</style>
</head>
<body>
<main class="menu">
  <div class="sketch sketch--left" role="img" aria-label="Hand-drawn sketch of a pizza edge"></div>
  <div class="sketch sketch--slice" role="img" aria-label="Hand-drawn sketch of a pepperoni pizza slice"></div>
  <div class="sketch sketch--crust" role="img" aria-label="Hand-drawn sketch of a pizza crust"></div>

  <h1 class="page-title">WOOD FIRED PIZZA</h1>
  <p class="intro">All our dough is made fresh daily in house with just four ingredients: water, flour,<br>salt and yeast. Baked to perfection in the wood over, Fern Lantern Pizza is the best in the county!</p>

  <div class="specialty-band">Our Specialty Pies <span class="price">Small $13</span> <span class="price">Large $17</span></div>

  <section class="pie pie--buffalo">
    <h2>The Buffalo Bird</h2>
    <p>Buffalo sauce, grilled chicken,<br>mozzarella and topped with<br>red onion for just the right finish.<br>Don't like onion? We'll leave it off!</p>
  </section>
  <section class="pie pie--hula">
    <h2>The Hula Hula</h2>
    <p>Sliced ham and Pineapple<br>and mozzarella. It doesn't get<br>any better! Ask for coconut,<br>if you're feeling crazy!</p>
  </section>
  <section class="pie pie--chicken">
    <h2>Chicken ‘Q</h2>
    <p>House made BBQ sauce from<br>Oak Ember BBQ, Grilled chicken and<br>mozzarella make this crowd favorite.</p>
  </section>

  <section class="build">
    <header class="build__head">
      <h2>Create Your Own</h2>
      <div class="price">Small $11 &nbsp; Large $15</div>
    </header>
    <div class="build__body">
      <div class="group">Choose from standard toppings for <span class="cost">$2.00</span>:<br>Pepperoni, Onion, Tomato, Garlic, Green Pepper, Mushroom, Sliced<br>or Chopped Tomato, Broccoli, Spinach, Sliced black olives</div>
      <div class="group">More Meats <span class="cost">$2.50</span>:<br>Meatball, Bacon, Sausage, Chicken, Ham</div>
      <div class="group"><span class="label">Specialty Toppings</span> <span class="cost">$3.00</span>:<br>Xtra Cheese, Pineapple, Feta, Ricotta, Kalamata Olives, Hot Peppers,<br>Coconut, Artichokes, Sun dried Tomato, Pesto</div>
      <div class="group">Gluten Free, available in Small size only- add <span class="cost">$2.00</span></div>
      <div class="group note"><span class="label">Fold It Up!</span><br>Turn your Pizza into a calzone, specialty<br>or build your own. Same price as a small.</div>
    </div>
  </section>
</main>
</body>
</html>
```